FAST TURN AROUND - Yoga & Sound Meditation Event Flyer

Our organization - Corvid Stewardship Circle - is currently looking for someone to create a flyer for an upcoming Yoga & Sound Meditation Event.

We are looking for the following deliverables:
Versions of the Flyer created for Social Media (Long Story & Square Post) that includes the following information. (Not including the categories)
Event Title: Corvid Sway & Hum Wind Down Edition - Lunaport Mixdown
Event Date & Time: Wednesday, April 20 | 7P - 9P
Event Location: Pebblehall at Fernway
Corvid Logo: (Both black and white versions are attached. Feel free to use whichever makes more sense based on the lighting)

We would want a version of this for the eight different background images provided. For the test, you can submit 1-2 since the rest of the details will be the same once we chose the information design.

```html
<!DOCTYPE html>
<html lang="en">
<head>
<meta charset="utf-8">
<title>Corvid Sway &amp; Hum Wind Down Edition – Lunaport Mixdown</title>
<link rel="stylesheet" href="https://fonts.googleapis.com/css2?family=Ultra&family=Open+Sans:wght@300;400&display=swap">
<style>
  :root {
    --green-top: #7ab848;
    --green-mid: #6aab40;
    --green-deep: #3e8c36;
    --lime-band: #a9cd2b;
    --lime-text: #e2ff14;
    --white: #ffffff;
    --photo-warm-1: #f4efe9;
    --photo-warm-2: #c9bfb4;
    --photo-warm-3: #8f7a68;
    --photo-leaf-1: #b9c98a;
    --photo-leaf-2: #7f9a55;
    --photo-leaf-3: #d9d2c8;
  }
  * { margin: 0; padding: 0; box-sizing: border-box; }
  html, body { width: 848px; height: 1200px; overflow: hidden; background: #ffffff; }
  .flyer {
    position: relative;
    width: 848px;
    height: 1200px;
    overflow: hidden;
    background: linear-gradient(180deg, var(--green-top) 0%, var(--green-mid) 55%, var(--green-deep) 100%);
    font-family: "Ultra", Georgia, serif;
    color: var(--white);
  }
  .flyer__artwork { position: absolute; top: 0; left: 0; width: 848px; height: 660px; }
  .text-line {
    position: absolute;
    left: 0;
    width: 100%;
    text-align: center;
    line-height: 1;
    white-space: nowrap;
  }
  .brand-name { top: 628px; font-size: 104px; letter-spacing: -1px; }
  .brand-tagline {
    top: 742px;
    font-family: "Open Sans", Arial, sans-serif;
    font-weight: 300;
    font-size: 30px;
  }
  .event-title { top: 818px; font-size: 27px; }
  .event-subtitle { top: 870px; font-size: 44px; color: var(--lime-text); }
  .info-label {
    font-size: 24px;
    text-decoration: underline;
    text-decoration-thickness: 2px;
    text-underline-offset: 4px;
  }
  .info-label--date { top: 954px; }
  .info-label--place { top: 1056px; }
  .info-value { color: var(--lime-text); }
  .info-value--date { top: 996px; font-size: 30px; }
  .info-value--place { top: 1100px; font-size: 38px; }
  .version-code {
    position: absolute;
    right: 14px;
    bottom: 8px;
    font-family: Arial, Helvetica, sans-serif;
    font-size: 22px;
    color: var(--white);
  }
</style>
</head>
<body>
<main class="flyer">
  <svg class="flyer__artwork" viewBox="0 0 848 660" xmlns="http://www.w3.org/2000/svg">
    <defs>
      <linearGradient id="studio-photo-tone" x1="0" y1="0" x2="1" y2="1">
        <stop offset="0" stop-color="var(--photo-warm-3)"/>
        <stop offset="0.35" stop-color="var(--photo-warm-1)"/>
        <stop offset="0.7" stop-color="var(--photo-warm-2)"/>
        <stop offset="1" stop-color="var(--photo-warm-3)"/>
      </linearGradient>
      <linearGradient id="garden-photo-tone" x1="0" y1="0" x2="1" y2="1">
        <stop offset="0" stop-color="var(--photo-leaf-2)"/>
        <stop offset="0.5" stop-color="var(--photo-leaf-1)"/>
        <stop offset="1" stop-color="var(--photo-leaf-3)"/>
      </linearGradient>
    </defs>

    <path class="wave-band" d="M0,252 C210,248 380,440 560,446 C720,452 820,380 848,262 V352 C800,470 700,500 590,486 C420,470 220,300 0,300 Z" fill="var(--lime-band)"/>

    <path role="img" aria-label="Photo of a sound meditation guide seated beside a table of candles and singing bowls"
          d="M0,0 H848 V262 C818,372 720,438 560,438 C380,434 210,258 0,262 Z"
          fill="url(#studio-photo-tone)"/>

    <path class="wave-line" d="M0,286 C210,278 380,436 560,444" fill="none" stroke="var(--white)" stroke-width="6"/>

    <path class="wave-band" d="M0,498 C60,580 140,622 230,622 C360,622 480,560 580,466 L600,470 C500,575 370,636 232,636 C130,636 50,590 0,530 Z" fill="var(--lime-band)"/>

    <path role="img" aria-label="Photo of a yoga instructor standing in front of greenery"
          d="M0,290 C210,282 380,440 566,450 C480,545 360,612 230,612 C140,612 60,572 0,500 Z"
          fill="url(#garden-photo-tone)"/>

    <path class="wave-band" d="M566,452 C700,470 800,420 848,330 V368 C810,470 720,504 600,494 Z" fill="var(--lime-band)"/>
  </svg>

  <div class="text-line brand-name">Corvid</div>
  <div class="text-line brand-tagline">Corvid Stewardship Circle</div>

  <h1 class="text-line event-title">Corvid Sway &amp; Hum Wind Down Edition</h1>
  <h2 class="text-line event-subtitle">Lunaport Mixdown</h2>

  <div class="text-line info-label info-label--date">EVENT DATE &amp; TIME</div>
  <div class="text-line info-value info-value--date">Wednesday, April 20 | 7P - 9P</div>

  <div class="text-line info-label info-label--place">EVENT LOCATION</div>
  <div class="text-line info-value info-value--place">Pebblehall at Fernway</div>

  <div class="version-code">C2</div>
</main>
</body>
</html>
```